Etiketten für Imkerei aus der Steiermark
Zielgruppe
Wir sind eine Imkerei aus der Steiermark / Österreich im Vollerwerb. www.lindtal-honig.at
Zielgruppe: Frauen, Familien, Regional
Unser Image: hohe Qualität, Familienbetrieb, naturnah, gesund
Vermarktung: Direkt, Verkaufsstellen, Märkte, zukünftig auch online
Aufgabenstellung
Wir werden die Honiggläser und die Druckerei umstellen und möchten hierfür ein profesionelles abgestimmtes Design. Unser Logo soll erhalten bleiben. Die Honigsortenbezeichnung (Waldhonig, Cremehonig, Blütenhonig) soll zukünftig eingedruckt werden und neben dem Logo ein Zentrales Element sein.
In Zukunft verwenden wir Vorsa Gläser mit hohen Deckel der Firma Balumo in den Größen 1000g(Ilka 785), 500g (Vor 410), 250 g (Vor 212) und 150 g (Vor 125). Der Deckel soll einheitlich Gold oder Silber sein.

```html
<!DOCTYPE html>
<html lang="de">
<head>
<meta charset="utf-8">
<title>Lindtal Honig – Etiketten</title>
<link href="https://fonts.googleapis.com/css2?family=Amatic+SC:wght@700&family=Quicksand:wght@500;700&family=Roboto+Condensed:wght@400&display=swap" rel="stylesheet">
<style>
  :root {
    --stage: #e2e2e2;
    --forest: #a3b936;
    --forest-soft: #bccd6a;
    --blossom: #cf5661;
    --blossom-soft: #e07d88;
    --cream: #e5c27c;
    --cream-soft: #eed39c;
    --ink: #2b2b2b;
    --paper: #ffffff;
    --logo-yellow: #fdf07a;
  }
  * { box-sizing: border-box; margin: 0; padding: 0; }
  html, body { width: 1095px; height: 1200px; overflow: hidden; }
  body { background: var(--stage); position: relative; font-family: "Quicksand", sans-serif; }

  .label {
    position: absolute;
    overflow: hidden;
    color: var(--paper);
    font-size: 11px;
  }
  .label--forest { background: var(--forest); }
  .label--blossom { background: var(--blossom); }
  .label--cream { background: var(--cream); }
  .label--large { font-size: 16px; }

  .motif {
    position: absolute;
    border-radius: 46% 46% 10% 10%;
  }
  .label--forest .motif { background: linear-gradient(180deg, var(--forest-soft), rgba(188,205,106,0.75)); }
  .label--blossom .motif { background: radial-gradient(circle, var(--blossom-soft) 55%, rgba(224,125,136,0) 72%); border-radius: 50%; }
  .label--cream .motif { background: linear-gradient(180deg, var(--cream-soft), rgba(238,211,156,0.8)); }

  .best-before {
    position: absolute; top: 5%; right: 3.5%;
    font-family: "Roboto Condensed", sans-serif;
    font-size: 0.72em;
  }
  .centre {
    position: absolute; left: 0; right: 0; top: 13%;
    text-align: center;
  }
  .variety {
    font-family: "Amatic SC", cursive;
    font-size: 3.9em;
    line-height: 1;
    color: var(--ink);
    letter-spacing: 0.01em;
  }
  .quality {
    font-size: 1.1em;
    letter-spacing: 0.06em;
    margin-top: 0.1em;
  }
  .weight {
    font-weight: 700;
    color: var(--ink);
    font-size: 1.05em;
    margin-top: 0.4em;
  }
  .brand {
    display: inline-flex; align-items: center; gap: 0.35em;
    margin-top: 1.4em;
  }
  .brand-dot {
    width: 2.6em; height: 2.6em; border-radius: 50%;
    background: var(--logo-yellow);
  }
  .brand-name {
    font-weight: 700; font-size: 1.25em; color: var(--ink);
  }
  .website {
    font-weight: 700; font-size: 0.78em; color: var(--ink);
    margin-top: 0.7em;
  }
  .contact, .storage {
    position: absolute; bottom: 6%;
    font-family: "Roboto Condensed", sans-serif;
    font-size: 0.8em; line-height: 1.3;
  }
  .contact { left: 3.5%; }
  .storage { right: 3.5%; text-align: right; }
</style>
</head>
<body>

  <!-- Cremehonig -->
  <section class="label label--cream" style="left:565px; top:253px; width:401px; height:240px;">
    <div class="motif" role="img" aria-label="Helle Illustration einer Cremehonig-Spirale" style="left:40%; top:0; width:36%; height:100%;"></div>
    <p class="best-before">Mindesten haltbar bis:</p>
    <div class="centre">
      <h2 class="variety">Cremehonig</h2>
      <p class="quality">Österreichischer Qualitätshonig</p>
      <p class="weight">150g</p>
      <div class="brand"><span class="brand-dot"></span><span class="brand-name">Lindtal Honig</span></div>
      <p class="website">www.lindtal-honig.at</p>
    </div>
    <p class="contact">Meisterimkerei Lindtal<br>Birkenweg 12<br>8142 Talbach<br>Tel: 0664 /55 12 340<br>post@lindtal-honig.at</p>
    <p class="storage">Trocken und vor Wärme<br>geschützt lagern!</p>
  </section>

  <!-- Waldhonig klein -->
  <section class="label label--forest" style="left:139px; top:370px; width:396px; height:238px;">
    <div class="motif" role="img" aria-label="Helle Illustration einer Tanne" style="left:46%; top:4%; width:38%; height:96%;"></div>
    <p class="best-before">Mindesten haltbar bis:</p>
    <div class="centre">
      <h2 class="variety">Waldhonig</h2>
      <p class="quality">Österreichischer Qualitätshonig</p>
      <p class="weight">150g</p>
      <div class="brand"><span class="brand-dot"></span><span class="brand-name">Lindtal Honig</span></div>
      <p class="website">www.lindtal-honig.at</p>
    </div>
    <p class="contact">Meisterimkerei Lindtal<br>Birkenweg 12<br>8142 Talbach<br>Tel: 0664 /55 12 340<br>post@lindtal-honig.at</p>
    <p class="storage">Trocken und vor Wärme<br>geschützt lagern!</p>
  </section>

  <!-- Blütenhonig -->
  <section class="label label--blossom" style="left:18px; top:633px; width:517px; height:238px;">
    <div class="motif" role="img" aria-label="Helle Illustration einer Blüte" style="left:40%; top:26%; width:37%; height:82%;"></div>
    <p class="best-before">Mindesten haltbar bis:</p>
    <div class="centre">
      <h2 class="variety">Blütenhonig</h2>
      <p class="quality">Österreichischer Qualitätshonig</p>
      <p class="weight">150g</p>
      <div class="brand"><span class="brand-dot"></span><span class="brand-name">Lindtal Honig</span></div>
      <p class="website">www.lindtal-honig.at</p>
    </div>
    <p class="contact">Meisterimkerei Lindtal<br>Birkenweg 12<br>8142 Talbach<br>Tel: 0664 /55 12 340<br>post@lindtal-honig.at</p>
    <p class="storage">Trocken und vor Wärme<br>geschützt lagern!</p>
  </section>

  <!-- Waldhonig groß -->
  <section class="label label--forest label--large" style="left:564px; top:519px; width:514px; height:428px;">
    <div class="motif" role="img" aria-label="Helle Illustration einer Tanne" style="left:26%; top:6%; width:70%; height:94%;"></div>
    <p class="best-before">Mindesten haltbar bis:</p>
    <div class="centre" style="top:18%;">
      <h2 class="variety">Waldhonig</h2>
      <p class="quality">Österreichischer Qualitätshonig</p>
      <p class="weight">150g</p>
      <div class="brand" style="margin-top:2.6em;"><span class="brand-dot"></span><span class="brand-name">Lindtal Honig</span></div>
      <p class="website">www.lindtal-honig.at</p>
    </div>
    <p class="contact">Meisterimkerei Lindtal<br>Birkenweg 12<br>8142 Talbach<br>Tel: 0664 /55 12 340<br>post@lindtal-honig.at</p>
    <p class="storage">Trocken und vor Wärme<br>geschützt lagern!</p>
  </section>

</body>
</html>
```